Startup Drone Platform Company business card

We are needing a business card design for our employees. We are a startup drone platform. We are looking for a business card that has our logo on one side, with the employee/company details on the opposite side. We are looking for something that is very eye catching, modern, and bold.

Target Market(s)

This will target both drone pilots and drone businesses, along with all the industries that could utilize drone services (aerial video, aerial photos, inspections, 3d mapping, etc).

Industry/Entity Type

Business

```html
<!DOCTYPE html>
<html lang="en">
<head>
<meta charset="utf-8">
<title>Aerolift Business Card</title>
<link href="https://fonts.googleapis.com/css2?family=Josefin+Sans:wght@300;400;600;700&display=swap" rel="stylesheet">
<style>
  :root {
    --backdrop: #34444b;
    --card: #f6f7f7;
    --ink: #161616;
    --teal: #3cbfc9;
    --muted: #3a3a3a;
  }
  * { margin: 0; padding: 0; box-sizing: border-box; }
  html, body {
    width: 1200px; height: 900px; overflow: hidden;
    background: var(--backdrop);
    font-family: "Josefin Sans", sans-serif;
    color: var(--ink);
  }
  .sheet {
    width: 1200px; height: 900px;
    display: flex; flex-direction: column; align-items: center; justify-content: center;
    gap: 40px;
  }
  .card {
    width: 700px; height: 400px;
    background: var(--card);
    position: relative;
    box-shadow: 0 10px 30px rgba(0,0,0,0.35);
  }

  /* Front: employee details */
  .person { position: absolute; left: 56px; top: 46px; }
  .person-name {
    font-size: 46px; font-weight: 300; letter-spacing: 1px; line-height: 1;
  }
  .person-name strong { font-weight: 700; }
  .person-role {
    margin-top: 8px; font-size: 19px; color: var(--teal); font-weight: 300; letter-spacing: 0.5px;
  }
  .person-role strong { font-weight: 700; }

  .contact-list { position: absolute; left: 56px; top: 170px; list-style: none; }
  .contact-item {
    display: flex; align-items: center; gap: 22px;
    font-size: 16px; color: var(--muted); margin-bottom: 22px; line-height: 1.25;
  }
  .contact-icon { width: 26px; height: 26px; flex: none; }
  .contact-icon svg { width: 26px; height: 26px; stroke: var(--teal); fill: none; stroke-width: 1.4; }

  .brand-stack {
    position: absolute; right: 50px; top: 150px;
    display: flex; flex-direction: column; align-items: center; gap: 18px;
  }
  .brand-dot {
    width: 90px; height: 90px; border-radius: 50%;
    border: 3px solid var(--teal);
  }
  .brand-name {
    font-size: 24px; font-weight: 600; letter-spacing: 8px; color: var(--ink);
    text-transform: uppercase;
  }

  /* Back: brand side */
  .brand-center {
    position: absolute; left: 0; right: 0; top: 160px;
    text-align: center;
    font-size: 40px; font-weight: 600; letter-spacing: 16px; text-transform: uppercase;
    color: var(--ink);
  }
  .web-address {
    position: absolute; left: 0; right: 0; bottom: 50px;
    text-align: center; font-size: 21px; font-weight: 300; color: var(--teal); letter-spacing: 0.5px;
  }
</style>
</head>
<body>
<main class="sheet">
  <section class="card card-front">
    <div class="person">
      <h1 class="person-name">MARCUS <strong>HALE</strong></h1>
      <p class="person-role"><strong>DIRECTOR</strong> OPERATIONS</p>
    </div>
    <ul class="contact-list">
      <li class="contact-item">
        <span class="contact-icon"><svg viewBox="0 0 26 26"><rect x="8" y="2" width="10" height="22" rx="2"/><line x1="11" y1="20.5" x2="15" y2="20.5"/></svg></span>
        +61 400 123 456
      </li>
      <li class="contact-item">
        <span class="contact-icon"><svg viewBox="0 0 26 26"><circle cx="13" cy="13" r="11"/><ellipse cx="13" cy="13" rx="5" ry="11"/><line x1="2" y1="13" x2="24" y2="13"/><path d="M4 7h18M4 19h18"/></svg></span>
        MarcusHale@aerolift.com
      </li>
      <li class="contact-item">
        <span class="contact-icon"><svg viewBox="0 0 26 26"><path d="M13 24C8 17 6 13.5 6 10a7 7 0 0 1 14 0c0 3.5-2 7-7 14z"/><circle cx="13" cy="10" r="2.5"/></svg></span>
        <span>48 Harbour View Road<br>Northgate Business Park</span>
      </li>
    </ul>
    <div class="brand-stack">
      <div class="brand-dot"></div>
      <div class="brand-name">Aerolift</div>
    </div>
  </section>

  <section class="card card-back">
    <div class="brand-center">Aerolift</div>
    <p class="web-address">www.aerolift.com</p>
  </section>
</main>
</body>
</html>
```